Bathroom Remodeling Guide Needed

We need to create a Bathroom remodeling guide that we can give away as a freemium download. The attached file contains the instructions and copy for the guide along with our logo. Below is a dropbox link to our assets folder as well.

https://www.filevaultora.net/sh/fo/k7trw2mzq9plv804bxnhe/QJTmVzaPwErKs5yUxLcHoBn4?key=7hfpt2c9048rwq1ma5517j39m&dl=0

```html
<!DOCTYPE html>
<html lang="en">
<head>
<meta charset="utf-8">
<title>Bathroom Remodeling Guide – Harbor Tile &amp; Bath</title>
<link href="https://fonts.googleapis.com/css2?family=Poppins:wght@300;400;500;600;700&display=swap" rel="stylesheet">
<style>
:root{
  --navy:#1d2f4d;
  --navy-deep:#13203a;
  --ink:#1a1a1a;
  --paper:#ffffff;
  --paper-soft:#f3f3f3;
  --stage:#dcdcdc;
  --photo-warm-a:#efe6da;
  --photo-warm-b:#b9a286;
  --photo-cool-a:#e9edf1;
  --photo-cool-b:#9ea9b6;
  --photo-dark-a:#2b2a26;
  --photo-dark-b:#5a4529;
}
*{margin:0;padding:0;box-sizing:border-box}
html,body{width:720px;height:1200px;overflow:hidden;background:var(--stage);font-family:'Poppins',sans-serif;color:var(--ink)}
.canvas{position:relative;width:720px;height:1200px}
.spread{position:absolute;left:99px;width:522px;height:370px;display:flex;box-shadow:0 4px 14px rgba(0,0,0,.18)}
.spread--covers{top:22px}
.spread--intro{top:415px}
.spread--costs{top:808px}
.page{position:relative;width:261px;height:370px;overflow:hidden;background:var(--paper)}
.photo{position:absolute}
.abs{position:absolute}
.brand{display:flex;align-items:center;gap:5px;font-weight:600;letter-spacing:.08em;text-transform:uppercase}
.brand__square{width:9px;height:9px;background:currentColor}
.url-band{position:absolute;height:15px;background:var(--navy-deep);color:#fff;font-size:5.5px;display:flex;align-items:center;padding:0 10px;letter-spacing:.02em}
.display{font-weight:300;text-transform:uppercase;line-height:1.18;letter-spacing:.01em}
.body{font-size:5.2px;line-height:1.45}
.list{list-style:none;font-size:5.2px;line-height:1.5}
.list li::before{content:"• "}

/* Back cover */
.back-cover__frame{position:absolute;inset:14px 14px 14px 14px;border:2px solid var(--navy)}
.back-cover__photo{left:0;right:0;bottom:0;height:175px;background:linear-gradient(180deg,rgba(255,255,255,1) 0%,var(--photo-warm-a) 35%,var(--photo-warm-b) 100%)}
.back-cover__brand{left:60px;top:62px;font-size:11px;color:var(--ink)}
.back-cover__title{left:30px;right:30px;top:100px;text-align:center;font-weight:700;font-size:14px;line-height:1.15;color:var(--navy);text-transform:uppercase}
.back-cover__text{left:28px;right:28px;top:140px;text-align:center;font-size:5.4px;line-height:1.5}
.back-cover__cta{left:20px;right:20px;top:168px;text-align:center;font-weight:700;font-size:9px}
.back-cover__place{left:20px;right:20px;top:182px;text-align:center;font-size:5.6px}

/* Front cover */
.cover__photo{inset:0;background:linear-gradient(160deg,var(--photo-cool-a),var(--photo-cool-b))}
.cover__brand{left:22px;top:38px;font-size:11px;color:var(--ink)}
.cover__band{left:0;right:0;top:150px;height:26px;background:var(--navy-deep);color:#fff;font-size:9.5px;display:flex;align-items:center;padding-left:20px}
.cover__block{left:0;top:176px;width:138px;height:160px;background:var(--navy);color:#fff;padding:18px 12px}
.cover__title{font-size:13px}
.cover__sub{margin-top:8px;font-size:5.6px;line-height:1.5}
.cover__aside{left:138px;top:176px;width:123px;height:70px;background:var(--paper);color:var(--navy);font-weight:300;font-size:11.5px;line-height:1.25;padding:10px 12px}

/* Intro spread */
.intro-left{background:var(--paper-soft)}
.intro-left__photo{left:22px;top:28px;width:210px;height:170px;background:linear-gradient(135deg,var(--photo-warm-a),#d7c3a8)}
.intro-left__box{left:111px;top:178px;width:150px;height:186px;background:var(--navy);color:#fff;padding:10px 10px;font-size:4.9px;line-height:1.42}
.intro-left__box p+p{margin-top:4px}
.intro-left__heading{left:22px;top:250px;font-size:13px;color:var(--navy)}
.intro-right{background:var(--paper-soft)}
.intro-right__band{left:0;right:0;top:0;height:28px;background:var(--navy-deep)}
.intro-right__heading{left:18px;top:42px;right:14px;font-size:11.5px;color:var(--navy)}
.intro-right__lead{left:18px;top:78px;right:18px;font-weight:700;font-size:5.6px;line-height:1.4}
.intro-right__body{left:18px;top:96px;width:128px}
.intro-right__photo{left:0;top:200px;width:190px;height:150px;background:linear-gradient(150deg,#f1f2f3,#a9b0b8)}
.intro-right__box{left:148px;top:128px;width:108px;height:214px;background:var(--navy);color:#fff;padding:10px 8px;border:5px solid var(--navy-deep);font-size:5px;line-height:1.42}
.intro-right__box h3{font-size:6.2px;font-weight:600;margin-bottom:4px;line-height:1.3}
.intro-right__box .list{font-size:5px;line-height:1.42}
.intro-right__box p{margin-top:5px}

/* Costs spread */
.costs-page{background:transparent}
.costs__photo{left:99px;top:808px;width:522px;height:370px;background:linear-gradient(120deg,var(--photo-dark-a) 0%,#3b3124 55%,var(--photo-dark-b) 100%)}
.costs-left__panel{left:0;right:0;bottom:0;height:110px;background:var(--paper);clip-path:polygon(0 18%,100% 0,100% 100%,0 100%)}
.costs-left__heading{left:18px;top:160px;font-size:12.5px;color:#fff}
.costs-left__text{left:18px;top:218px;right:14px;color:#fff}
.costs-left__price{left:18px;top:240px;right:14px;color:#fff;font-size:5.4px}
.costs-left__price b{font-size:7.5px}
.costs-left__factors{left:18px;top:282px;right:14px}
.costs-left__factors h4{font-size:6.2px;font-weight:700;margin-bottom:3px}
.cols{display:flex;gap:8px}
.costs-left__note{margin-top:4px}
.costs-right__panel{left:0;right:0;bottom:0;height:150px;background:var(--paper);clip-path:polygon(0 6%,100% 0,100% 100%,0 100%)}
.costs-right__heading{left:14px;top:110px;right:10px;font-size:11.5px;color:#fff}
.costs-right__lead{left:14px;top:160px;right:10px;color:#fff;font-size:5px}
.costs-right__body{left:14px;top:232px;right:14px}
.costs-right__body p+p{margin-top:4px}
</style>
</head>
<body>
<main class="canvas">

  <section class="spread spread--covers">
    <article class="page back-cover">
      <div class="photo back-cover__photo" role="img" aria-label="Photo of a warm luxury bathroom with freestanding tub and glass shower"></div>
      <div class="back-cover__frame"></div>
      <div class="abs brand back-cover__brand"><span class="brand__square"></span>Harbor Tile &amp; Bath</div>
      <h2 class="abs back-cover__title">Let's Design<br>Your Bathroom</h2>
      <p class="abs back-cover__text">The best place to start is with a conversation.<br>We'll help you clarify your vision, explore your options, and create a plan tailored specifically to your home.</p>
      <p class="abs back-cover__cta">Schedule Your Design Consultation</p>
      <p class="abs back-cover__place">Harbor Tile &amp; Bath Charlotte, NC</p>
    </article>
    <article class="page cover">
      <div class="photo cover__photo" role="img" aria-label="Photo of a bright white bathroom with freestanding tub and navy vanity"></div>
      <div class="abs brand cover__brand"><span class="brand__square"></span>Harbor Tile &amp; Bath</div>
      <div class="abs cover__band">The Homeowner's Guide to</div>
      <div class="abs cover__block">
        <h1 class="display cover__title">Bathroom<br>Remodeling<br>in Charlotte</h1>
        <p class="cover__sub">How to Plan, Design, and Build a Bathroom You'll Love for Years to Come</p>
      </div>
      <p class="abs cover__aside">Harbor Tile<br>&amp; Bath</p>
    </article>
  </section>

  <section class="spread spread--intro">
    <article class="page intro-left">
      <div class="photo intro-left__photo" role="img" aria-label="Photo of a cream bathroom with arched niche, round mirror and tub"></div>
      <div class="url-band" style="left:0;top:22px;width:130px">www.harbortilebath.com</div>
      <div class="abs intro-left__box">
        <p>Remodeling your bathroom is one of the most impactful upgrades you can make to your home. Done right, it improves how you start and end your day, increases your home's value, and creates a space that feels both functional and refined.</p>
        <p>But without the right plan, it can quickly become overwhelming.</p>
        <p>Many homeowners begin with inspiration photos and good intentions, only to run into unexpected costs, delays, and decisions they weren't prepared for.</p>
        <p>This guide was created to give you clarity before you begin, so you can move forward with confidence, avoid common mistakes, and achieve a result you'll be proud of for years to come.</p>
      </div>
      <h2 class="abs display intro-left__heading">Before you<br>start your<br>bathroom<br>remodel</h2>
    </article>
    <article class="page intro-right">
      <div class="abs intro-right__band"></div>
      <div class="url-band" style="right:0;top:6px;width:120px;justify-content:flex-end">www.harbortilebath.com</div>
      <h2 class="abs display intro-right__heading">Most bathroom remodels go wrong before they even start</h2>
      <p class="abs intro-right__lead">The success of a bathroom remodel is determined long before construction begins.</p>
      <p class="abs body intro-right__body">The most common mistake homeowners make is starting without a clear, well-thought-out plan. Decisions are made on the fly, materials are selected too late, and small issues quickly turn into costly problems.</p>
      <div class="photo intro-right__photo" role="img" aria-label="Photo of a marble walk-in glass shower in a white bathroom"></div>
      <div class="abs intro-right__box">
        <h3>A Successful Project Requires:</h3>
        <ul class="list">
          <li>A clear design vision</li>
          <li>Thoughtful material selection</li>
          <li>Proper planning before demolition</li>
          <li>A team that understands both design and construction</li>
        </ul>
        <p>When these elements are in place, the process becomes smooth, predictable, and even enjoyable.</p>
        <p>When they're not, the experience is often the opposite.</p>
      </div>
    </article>
  </section>

  <div class="photo costs__photo" role="img" aria-label="Dark photo of a modern bathroom with wood slat wall and plants"></div>
  <section class="spread spread--costs">
    <article class="page costs-page">
      <div class="url-band" style="left:0;top:22px;width:120px">www.harbortilebath.com</div>
      <h2 class="abs display costs-left__heading">Understanding<br>bathroom<br>remodeling costs</h2>
      <p class="abs body costs-left__text">Every bathroom remodel is unique, but most projects fall within a predictable range depending on size, scope, and finishes.</p>
      <p class="abs costs-left__price">At Harbor Tile &amp; Bath, most bathroom remodeling <b>PROJECTS START AT $35,000</b> and increase based on complexity, materials, and customization.</p>
      <div class="abs costs-left__panel"></div>
      <div class="abs costs-left__factors">
        <h4>Several factors influence the total investment:</h4>
        <div class="cols">
          <ul class="list">
            <li>The size of the space</li>
            <li>Plumbing or layout changes</li>
            <li>Specialty features such as walk-in showers or freestanding tubs</li>
          </ul>
          <ul class="list">
            <li>Tile selection and layout complexity</li>
            <li>Custom vanities and cabinetry</li>
            <li>Lighting and fixture upgrades</li>
          </ul>
        </div>
        <p class="body costs-left__note">Rather than focusing on the lowest possible cost, our approach is to deliver long-term value, combining thoughtful design, quality materials, and expert craftsmanship.</p>
      </div>
    </article>
    <article class="page costs-page">
      <div class="url-band" style="right:0;top:6px;width:120px;justify-content:flex-end">www.harbortilebath.com</div>
      <h2 class="abs display costs-right__heading">Why design is the foundation of a successful remodel</h2>
      <p class="abs costs-right__lead">A beautiful bathroom doesn't happen by accident—it is designed.</p>
      <div class="abs costs-right__panel"></div>
      <div class="abs body costs-right__body">
        <p>Layout, lighting, storage, and material selection must all work together to create a space that feels cohesive and functions effortlessly.</p>
        <p>Every project we take on includes a professional designer at no additional cost. This ensures that your bathroom is carefully planned before construction begins, eliminating guesswork and reducing the likelihood of costly changes later.</p>
        <p>With a clear design in place, you'll be able to visualize your new space, make confident decisions, and move into construction with clarity.</p>
      </div>
    </article>
  </section>

</main>
</body>
</html>
```